Automotive eCommerce Business looking for a business card design

Looking for a clean and simple business card design. Our company name is "Harbor Crest Auto" and we are a company specializing in the ecommerce sales of automotive parts, specifically for pick up trucks and large SUVs. Our company colours are red, black, and white.

Feel free to use the logo provided or create a new logo that you seem fit. Looking forward to your creative ideas!

Industry/Entity Type

Automotive

Contact Information for Business Card

We were thinking of a possibly two-sided design featuring just the logo and company name on one side, and personal information on the other side. Single sided designs will be considered as well.

Font styles to use
Serif
Sans Serif
Decorative

Colors
ec1f27
ffffff
000000

Requirements
Must have
• Space for employee's name, title, phone number and email address, along with the company address and website somewhere.

```html
<!DOCTYPE html>
<html lang="en">
<head>
<meta charset="utf-8">
<title>Harbor Crest Auto – Business Card</title>
<link href="https://fonts.googleapis.com/css2?family=Open+Sans:wght@400;600;700&display=swap" rel="stylesheet">
<style>
  :root {
    --brand-red: #ec1f27;
    --ink: #111111;
    --ink-soft: #222222;
    --paper: #ffffff;
    --backdrop: #2c2c2c;
    --card-w: 700px;
    --card-h: 400px;
  }
  * { box-sizing: border-box; margin: 0; padding: 0; }
  html, body {
    width: 1200px; height: 960px; overflow: hidden;
    background: var(--backdrop);
    font-family: "Open Sans", Arial, sans-serif;
  }
  .sheet {
    width: 1200px; height: 960px;
    display: flex; flex-direction: column;
    align-items: center; justify-content: center; gap: 60px;
  }
  .card {
    width: var(--card-w); height: var(--card-h);
    background: var(--paper);
    position: relative;
  }

  /* Front: company name */
  .card--front {
    display: flex; align-items: center; justify-content: center;
  }
  .brand {
    display: flex; align-items: center; gap: 18px;
  }
  .brand__mark {
    width: 46px; height: 46px; background: var(--brand-red);
  }
  .brand__name {
    font-weight: 700; font-size: 34px; letter-spacing: 1px;
    color: var(--ink); text-transform: uppercase;
  }

  /* Back: personal details */
  .card--back .brand {
    position: absolute; left: 60px; top: 60px;
  }
  .card--back .brand__mark { width: 34px; height: 34px; }
  .card--back .brand__name { font-size: 24px; color: var(--brand-red); }

  .details {
    position: absolute; left: 330px; top: 150px;
  }
  .details__name {
    font-weight: 700; font-size: 28px; color: var(--brand-red);
    text-transform: uppercase; line-height: 1.1;
  }
  .details__title {
    font-size: 18px; color: var(--ink-soft); margin-bottom: 16px;
  }
  .contact {
    list-style: none;
    font-size: 18px; color: var(--ink-soft); line-height: 1.5;
  }
  .contact__item { display: flex; align-items: center; gap: 10px; }
  .contact__icon { width: 14px; height: 14px; fill: var(--brand-red); flex: none; }
  .contact__address { padding-left: 0; margin-top: 2px; }
</style>
</head>
<body>
  <main class="sheet">
    <section class="card card--front" aria-label="Card front">
      <div class="brand">
        <span class="brand__mark"></span>
        <span class="brand__name">Harbor Crest Auto Ltd.</span>
      </div>
    </section>

    <section class="card card--back" aria-label="Card back">
      <div class="brand">
        <span class="brand__mark"></span>
        <span class="brand__name">Harbor Crest Auto</span>
      </div>

      <div class="details">
        <h1 class="details__name">Marcus Delaney</h1>
        <p class="details__title">Managing Director</p>
        <ul class="contact">
          <li class="contact__item">
            <svg class="contact__icon" viewBox="0 0 16 16" aria-hidden="true"><path d="M3.5 1.5l2.5 0 1 3.5-1.6 1.2a8 8 0 0 0 4.4 4.4L11 9l3.5 1v2.5c0 .8-.7 1.5-1.5 1.5C7 14 2 9 2 3c0-.8.7-1.5 1.5-1.5z"/></svg>
            504 218 6630
          </li>
          <li class="contact__item">
            <svg class="contact__icon" viewBox="0 0 16 16" aria-hidden="true"><path d="M1 3h14v10H1z M1.6 3.6 8 9l6.4-5.4" fill="none" stroke="#ec1f27" stroke-width="1.6"/></svg>
            marcus@harborcrestauto.com
          </li>
          <li class="contact__item">
            <svg class="contact__icon" viewBox="0 0 16 16" aria-hidden="true"><path d="M8 1a5 5 0 0 0-5 5c0 3.8 5 9 5 9s5-5.2 5-9a5 5 0 0 0-5-5zm0 7a2 2 0 1 1 0-4 2 2 0 0 1 0 4z"/></svg>
            www.harborcrestauto.com
          </li>
          <li class="contact__address">418 Marlin Ridge Rd</li>
          <li class="contact__address">Port Ellis, LA 70512</li>
        </ul>
      </div>
    </section>
  </main>
</body>
</html>
```